bottle label/ product label for smoothies (ultra fresh)

Please create a bottle label for our smoothies for retail distribution.
It's important that the following key features are clearly stated:

Ultra-fresh

Handmade

No preservatives

Not heat-treated

No added sugar

The base of the product label should be transparent, so that the color and content of the smoothie can be seen clearly.

We are a young, dynamic company. Our values are honesty, ultra-freshness, and authenticity — and we are the only ones producing this type of product in our country. We are positioned in the premium segment.

Design style: Modern, clean, and natural — but not playful or childish.

Example product: Kelu Kelu (Mango, Pineapple, Lemon, Passion Fruit, Orange)

Wenn du möchtest, kann ich auch gleich einen konkreten Vorschlag für das Etikettendesign auf Englisch oder einen Entwurfstext für das Label selbst erstellen. Sag einfach Bescheid!

Target Market(s)

trade - convenience

Industry/Entity Type

trade

Font styles to use
Sans Serif

Requirements
Must have
• sales- features: Ultra-fresh Handmade No preservatives Not heat-treated No added sugar

```html
<!DOCTYPE html>
<html lang="en">
<head>
<meta charset="utf-8">
<title>Kelu Kelu Smoothie Labels</title>
<link rel="stylesheet" href="https://fonts.googleapis.com/css2?family=Oswald:wght@400;500&family=Nunito:wght@700&display=swap">
<style>
  :root {
    --page: #ffffff;
    --brand-green: #3f8a3a;
    --orange-bg: #f2d175;
    --orange-ink: #e5891e;
    --orange-band: #e28a22;
    --lemon-bg: #f4da7a;
    --lemon-ink: #d9ad12;
    --lemon-band: #e4c223;
    --passion-bg: #f1c0d4;
    --passion-ink: #6c1636;
    --passion-band: #6c1636;
  }
  * { box-sizing: border-box; margin: 0; padding: 0; }
  html, body { width: 1200px; height: 1200px; overflow: hidden; background: var(--page); }
  .canvas {
    width: 1200px; height: 1200px;
    display: flex; justify-content: center; align-items: center; gap: 60px;
  }
  .label {
    position: relative;
    width: 320px; height: 340px;
    background: var(--label-bg);
    overflow: hidden;
    border-radius: 4px;
  }
  .label--orange { --label-bg: var(--orange-bg); --ink: var(--orange-ink); --band: var(--orange-band); }
  .label--lemon { --label-bg: var(--lemon-bg); --ink: var(--lemon-ink); --band: var(--lemon-band); }
  .label--passion { --label-bg: var(--passion-bg); --ink: var(--passion-ink); --band: var(--passion-band); }

  .content {
    position: absolute; left: 16px; right: 16px; top: 8px;
    display: flex; flex-direction: column; align-items: center;
  }
  .brand {
    font-family: "Nunito", sans-serif; font-weight: 700;
    font-size: 28px; line-height: 1; color: var(--brand-green);
    padding: 12px 0 6px;
  }
  .range-name {
    font-family: "Oswald", sans-serif; font-weight: 400;
    font-size: 15px; line-height: 1.2; letter-spacing: 3px;
    color: var(--ink); text-transform: uppercase;
    margin-bottom: 6px;
  }
  .product {
    font-family: "Oswald", sans-serif; font-weight: 500;
    font-size: 26px; line-height: 1.05; text-align: center;
    color: var(--ink); text-transform: uppercase;
  }
  .fruit-art {
    width: 118px; height: 70px; margin: 10px 0 8px;
    border-radius: 40px;
    background: var(--art);
  }
  .label--orange .fruit-art { --art: radial-gradient(circle at 55% 55%, #e8501e, #f08a2a 60%, transparent 72%); }
  .label--lemon .fruit-art { --art: radial-gradient(circle at 55% 55%, #f5e04a, #f6e88a 60%, transparent 72%); }
  .label--passion .fruit-art { --art: radial-gradient(circle at 50% 55%, #7d3a78, #4b8a3a 60%, transparent 72%); }
  .claims {
    font-family: "Oswald", sans-serif; font-weight: 400;
    font-size: 10.5px; line-height: 1.35; text-align: center;
    color: var(--ink); text-transform: uppercase;
  }
  .band {
    position: absolute; left: 0; right: 0; bottom: 0; height: 52px;
  }
  .band svg { display: block; width: 100%; height: 100%; }
  .volume {
    position: absolute; bottom: 14px; left: 140px;
    width: 40px; height: 40px; border-radius: 50%;
    background: var(--band); border: 2px solid rgba(255,255,255,0.8);
    display: flex; align-items: center; justify-content: center;
    font-family: "Nunito", sans-serif; font-weight: 700;
    font-size: 10px; color: #fff;
  }
</style>
</head>
<body>
<main class="canvas">

  <article class="label label--orange">
    <div class="content">
      <div class="brand">verano</div>
      <div class="range-name">Kelu Kelu</div>
      <h2 class="product">Orange<br>Smoothie</h2>
      <div class="fruit-art" role="img" aria-label="Illustration of oranges with a leaf and a slice"></div>
      <p class="claims">No preservatives · Not heat treated<br>No added sugar · Vegetarian<br>Ultra-fresh · Handmade</p>
    </div>
    <div class="band">
      <svg viewBox="0 0 320 52" preserveAspectRatio="none"><path d="M0 14 C40 14 60 26 90 20 C120 14 140 24 170 24 C200 24 220 10 250 16 C280 22 300 12 320 14 L320 52 L0 52 Z" fill="var(--band)"/></svg>
    </div>
    <div class="volume">500ml</div>
  </article>

  <article class="label label--lemon">
    <div class="content">
      <div class="brand">verano</div>
      <div class="range-name">Kelu Kelu</div>
      <h2 class="product">Lemon<br>Smoothie</h2>
      <div class="fruit-art" role="img" aria-label="Illustration of lemons with a leaf and a slice"></div>
      <p class="claims">No preservatives · Not heat treated<br>No added sugar · Vegetarian<br>Ultra-fresh · Handmade</p>
    </div>
    <div class="band">
      <svg viewBox="0 0 320 52" preserveAspectRatio="none"><path d="M0 14 C40 14 60 26 90 20 C120 14 140 24 170 24 C200 24 220 10 250 16 C280 22 300 12 320 14 L320 52 L0 52 Z" fill="var(--band)"/></svg>
    </div>
    <div class="volume">500ml</div>
  </article>

  <article class="label label--passion">
    <div class="content">
      <div class="brand">verano</div>
      <div class="range-name">Kelu Kelu</div>
      <h2 class="product">Passionfruit<br>Smoothie</h2>
      <div class="fruit-art" role="img" aria-label="Illustration of passion fruit with leaves and a flower"></div>
      <p class="claims">No preservatives · Not heat treated<br>No added sugar · Vegetarian<br>Ultra-fresh · Handmade</p>
    </div>
    <div class="band">
      <svg viewBox="0 0 320 52" preserveAspectRatio="none"><path d="M0 14 C40 14 60 26 90 20 C120 14 140 24 170 24 C200 24 220 10 250 16 C280 22 300 12 320 14 L320 52 L0 52 Z" fill="var(--band)"/></svg>
    </div>
    <div class="volume">500ml</div>
  </article>

</main>
</body>
</html>
```